Cloud Based Internet Protection Service Business Cards

I would like a professionally designed business card. I already have a logo which I have attached.

The business is an online cloud based internet protection service aimed parents, particularly at non-technical parents and also schools.

The card should be be quite simple in its design, not to full of text and give its information in a clear and concise manner

Target Market(s)

Parents (especially non-technical parents) and also schools

Industry/Entity Type

Internet

Colors

Designer to choose colors to be used in the design.

Requirements
Should not have
• Too much text or be too cluttered. No decorative fonts, just a clear and concise font.

```html
<!DOCTYPE html>
<html lang="en">
<head>
<meta charset="utf-8">
<title>SafeNest Guard – Business Card</title>
<link href="https://fonts.googleapis.com/css2?family=Open+Sans:wght@400;600;700&display=swap" rel="stylesheet">
<style>
  :root {
    --canvas: #e4e5e7;
    --card-front: #ffffff;
    --card-back: #efefef;
    --navy: #0d3b56;
    --blue: #2a7db8;
    --ink: #1c2b36;
    --muted: #45535d;
    --light: #ffffff;
  }
  * { margin: 0; padding: 0; box-sizing: border-box; }
  html, body {
    width: 1200px; height: 675px; overflow: hidden;
    background: var(--canvas);
    font-family: "Open Sans", Arial, sans-serif;
  }
  .stage {
    position: relative; width: 1200px; height: 675px;
    display: flex; align-items: center; justify-content: center; gap: 50px;
  }
  .card {
    position: relative; width: 525px; height: 300px; overflow: hidden;
    box-shadow: 0 6px 18px rgba(0,0,0,0.12);
  }
  .card-front { background: var(--card-front); }
  .card-back { background: var(--card-back); }
  .card-bands { position: absolute; inset: 0; width: 100%; height: 100%; }

  .brand {
    position: absolute; display: flex; align-items: center; gap: 12px;
    color: var(--navy); font-weight: 700; letter-spacing: 0.5px;
  }
  .brand-dot {
    width: 40px; height: 40px; border-radius: 50%; background: var(--blue);
  }
  .card-front .brand { left: 0; right: 0; top: 112px; justify-content: center; font-size: 34px; }
  .card-back .brand { left: 34px; top: 82px; font-size: 30px; }
  .card-back .brand-dot { width: 34px; height: 34px; }

  .holder { position: absolute; right: 28px; top: 104px; text-align: right; }
  .holder-name { font-size: 14px; font-weight: 700; color: var(--ink); }
  .holder-title { font-size: 11px; color: var(--muted); }

  .website {
    position: absolute; right: 24px; top: 174px;
    font-size: 12px; color: var(--light);
  }
  .contact {
    position: absolute; left: 22px; bottom: 14px; list-style: none;
    color: var(--light); font-size: 12.5px; line-height: 19px;
  }
  .contact li { display: flex; align-items: center; gap: 8px; }
  .contact svg { width: 11px; height: 11px; fill: var(--light); flex: none; }
  .contact .phones { gap: 6px; }
</style>
</head>
<body>
<main class="stage">

  <section class="card card-front" aria-label="Card front">
    <svg class="card-bands" viewBox="0 0 525 300" preserveAspectRatio="none" aria-hidden="true">
      <polygon points="0,268 320,268 334,256 525,256 525,262 338,262 326,276 0,276" fill="var(--navy)"/>
      <polygon points="334,256 525,256 525,250 340,250" fill="var(--blue)"/>
    </svg>
    <div class="brand"><span class="brand-dot"></span>SafeNest Guard</div>
  </section>

  <section class="card card-back" aria-label="Card back">
    <svg class="card-bands" viewBox="0 0 525 300" preserveAspectRatio="none" aria-hidden="true">
      <polygon points="300,158 525,158 525,196 338,196" fill="var(--blue)"/>
      <polygon points="0,220 0,300 525,300 525,300 0,300" fill="var(--navy)"/>
      <polygon points="0,228 280,158 300,158 338,196 525,196 525,196 338,196 345,206 300,300 0,300" fill="var(--navy)"/>
    </svg>

    <div class="brand"><span class="brand-dot"></span>SafeNest Guard</div>

    <div class="holder">
      <p class="holder-name">Your Long Name</p>
      <p class="holder-title">Your Title</p>
    </div>

    <p class="website">www.yourwebsite.com</p>

    <ul class="contact">
      <li>
        <svg viewBox="0 0 12 12" aria-hidden="true"><path d="M6 0a4 4 0 0 0-4 4c0 3 4 8 4 8s4-5 4-8a4 4 0 0 0-4-4zm0 5.5A1.5 1.5 0 1 1 6 2.5a1.5 1.5 0 0 1 0 3z"/></svg>
        Your office or home long address
      </li>
      <li class="phones">
        <svg viewBox="0 0 12 12" aria-hidden="true"><path d="M1 4c0-2 2-3 5-3s5 1 5 3l-2 1-1-1.5H4L3 5zM2 6h8l1 5H1z"/></svg>
        000-000-0000
        <svg viewBox="0 0 12 12" aria-hidden="true"><path d="M3 0h6v12H3zm1 1v8h4V1z"/></svg>
        0000000000
      </li>
      <li>
        <svg viewBox="0 0 12 12" aria-hidden="true"><path d="M0 2h12v8H0zm1 1v.3l5 3.4 5-3.4V3z"/></svg>
        yourname@yourwebsite.com
      </li>
    </ul>
  </section>

</main>
</body>
</html>
```